Gobo Flyer to generate sales and to use at trade shows or as a leave behind to client

We are looking to create a flyer to promote our new exterior or interior event lighting options. We are looking for the layout to be clean and consistent with our color scheme. We are a professional technologically advanced company looking to take your event to the next level. We are looking for a layout which has an image at the top as well as a few other images to allow reader to see a few options

Target Market(s)

Residential as well as commercial

Industry/Entity Type

Trade

Requirements
Must have
• Need the round images to create a collage. and include the text samples of what is available

```html
<!DOCTYPE html>
<html lang="en">
<head>
<meta charset="utf-8">
<title>Projected Illuminations Flyer</title>
<link rel="stylesheet" href="https://fonts.googleapis.com/css2?family=Pacifico&family=Lato:ital,wght@0,300;0,400;0,700;1,400;1,700&family=Raleway:wght@300&family=Montserrat:wght@800;900&display=swap">
<style>
  :root {
    --page-bg: #d9d9d9;
    --flyer-bg: #0a0a0c;
    --brand-blue: #27a9e1;
    --accent-yellow: #fff200;
    --text-white: #ffffff;
    --text-soft: #d6d6d6;
    --bokeh-red: rgba(170, 30, 60, 0.45);
    --bokeh-gold: rgba(200, 170, 90, 0.35);
  }
  * { box-sizing: border-box; margin: 0; padding: 0; }
  html, body { width: 1200px; height: 900px; overflow: hidden; }
  body { background: var(--page-bg); position: relative; }

  .flyer {
    position: absolute; left: 295px; top: 20px;
    width: 610px; height: 860px; overflow: hidden;
    background:
      radial-gradient(circle at 92% 12%, var(--bokeh-red), transparent 32%),
      radial-gradient(circle at 14% 14%, var(--bokeh-gold), transparent 22%),
      radial-gradient(circle at 96% 40%, rgba(150, 20, 50, 0.3), transparent 22%),
      var(--flyer-bg);
    color: var(--text-white);
  }

  .title-line {
    position: absolute; left: 0; width: 100%; text-align: center;
    font-family: "Pacifico", cursive; color: var(--brand-blue);
    line-height: 1; letter-spacing: -1px;
  }
  .title-line--first { top: 18px; font-size: 66px; }
  .title-line--second { top: 96px; font-size: 70px; }

  .tagline {
    position: absolute; top: 176px; width: 100%; text-align: center;
    font-family: "Lato", sans-serif; font-weight: 300; font-size: 35px; line-height: 1;
  }
  .occasions {
    position: absolute; top: 216px; width: 100%; text-align: center;
    font-family: "Raleway", sans-serif; font-weight: 300; font-size: 20px;
    line-height: 22px; color: var(--text-soft);
  }
  .celebrate {
    position: absolute; top: 254px; width: 100%; text-align: center;
    font-family: "Pacifico", cursive; color: var(--accent-yellow);
    font-size: 30px; line-height: 1.2;
  }

  .snapshot {
    position: absolute; top: 312px; width: 178px; height: 166px;
    background: #fff; padding: 6px;
    box-shadow: 0 4px 10px rgba(0,0,0,0.6);
  }
  .snapshot--left { left: 44px; transform: rotate(5deg); }
  .snapshot--middle { left: 196px; top: 308px; width: 182px; transform: rotate(-1deg); }
  .snapshot--right { left: 362px; transform: rotate(-5deg); }
  .snapshot__image { width: 100%; height: 100%; }
  .snapshot--left .snapshot__image { background: linear-gradient(180deg, #1a1420 0%, #a0307a 45%, #6b4a3a 70%, #2a2016 100%); }
  .snapshot--middle .snapshot__image { background: linear-gradient(90deg, #c23a2a 0%, #6a4a50 50%, #2a3ad0 100%); }
  .snapshot--right .snapshot__image { background: linear-gradient(180deg, #1a1020 0%, #b040d0 45%, #6a4a40 72%, #2a2016 100%); }
  .snapshot__pin { position: absolute; top: -12px; left: 50%; margin-left: -10px; }

  .feature-photo {
    position: absolute; left: 0; top: 478px; width: 360px; height: 300px;
    background:
      radial-gradient(ellipse at 35% 30%, rgba(230, 40, 60, 0.75), transparent 55%),
      linear-gradient(180deg, #1a0a10 0%, #5a1630 40%, #9a4aa8 70%, #2a1030 100%);
    -webkit-mask-image: linear-gradient(90deg, #000 70%, transparent 100%), linear-gradient(180deg, #000 80%, transparent 100%);
    -webkit-mask-composite: source-in;
    mask-image: linear-gradient(90deg, #000 70%, transparent 100%);
  }

  .divider {
    position: absolute; left: 286px; top: 508px; width: 287px;
    border-top: 2px dotted #bfbfbf;
  }
  .description {
    position: absolute; right: 38px; top: 516px; width: 266px; text-align: right;
    font-family: "Lato", sans-serif; font-size: 12px; line-height: 15.4px;
  }

  .price-box {
    position: absolute; left: 356px; top: 626px; width: 201px; height: 130px;
    border: 2px solid #fff; border-radius: 8px; background: var(--flyer-bg);
    text-align: center; font-family: "Lato", sans-serif;
  }
  .price-box__heading {
    position: absolute; top: -12px; left: 50%; transform: translateX(-50%);
    background: var(--flyer-bg); padding: 0 3px; white-space: nowrap;
    font-weight: 700; font-size: 17px; line-height: 20px;
  }
  .price-box__from {
    margin-top: 8px; color: var(--accent-yellow); font-weight: 700; font-size: 15px; line-height: 16px;
  }
  .price-box__amount {
    font-family: "Montserrat", sans-serif; font-weight: 900; color: var(--accent-yellow);
    font-size: 64px; line-height: 62px; letter-spacing: -2px;
  }
  .price-box__terms {
    font-style: italic; font-weight: 700; font-size: 10.5px; line-height: 13px;
  }

  .brand {
    position: absolute; left: 36px; top: 800px; display: flex; align-items: center; gap: 8px;
    font-family: "Lato", sans-serif; font-weight: 700; font-size: 22px; color: var(--brand-blue);
    letter-spacing: 1px;
  }
  .brand__mark { width: 18px; height: 18px; background: var(--brand-blue); }

  .phone {
    position: absolute; right: 27px; top: 772px;
    font-family: "Montserrat", sans-serif; font-weight: 900; font-size: 36px;
    color: var(--brand-blue); line-height: 1;
  }
  .website {
    position: absolute; right: 31px; top: 814px;
    font-family: "Lato", sans-serif; font-size: 19px; line-height: 1;
  }
</style>
</head>
<body>
  <main class="flyer">
    <h1>
      <span class="title-line title-line--first">Projected</span>
      <span class="title-line title-line--second">Illuminations</span>
    </h1>
    <p class="tagline">Perfect for Special Events</p>
    <p class="occasions">Parties | Graduation | Holidays<br>Weddings | Business Promotions</p>
    <p class="celebrate">Anytime you want to celebrate</p>

    <figure class="snapshot snapshot--left">
      <div class="snapshot__image" role="img" aria-label="House exterior lit in pink with a projected light design"></div>
      <svg class="snapshot__pin" width="20" height="22" viewBox="0 0 20 22"><circle cx="12" cy="7" r="6" fill="#2f7fd6"/><line x1="9" y1="11" x2="3" y2="20" stroke="#ccc" stroke-width="2"/></svg>
    </figure>
    <figure class="snapshot snapshot--middle">
      <div class="snapshot__image" role="img" aria-label="House exterior lit in red, white and blue for a holiday"></div>
      <svg class="snapshot__pin" width="20" height="22" viewBox="0 0 20 22"><circle cx="12" cy="7" r="6" fill="#2f7fd6"/><line x1="9" y1="11" x2="3" y2="20" stroke="#ccc" stroke-width="2"/></svg>
    </figure>
    <figure class="snapshot snapshot--right">
      <div class="snapshot__image" role="img" aria-label="House exterior lit in purple with a greeting projected on the driveway"></div>
      <svg class="snapshot__pin" width="20" height="22" viewBox="0 0 20 22"><circle cx="12" cy="7" r="6" fill="#2f7fd6"/><line x1="9" y1="11" x2="3" y2="20" stroke="#ccc" stroke-width="2"/></svg>
    </figure>

    <div class="feature-photo" role="img" aria-label="Home facade washed in purple light with projected red hearts"></div>

    <hr class="divider">
    <p class="description">Illuminate a projected light design and 2 colored wall washers on the exterior or interior of your home business or special event.&nbsp; Choose from many stock designs or customize the image to make the design truly your own.</p>

    <section class="price-box">
      <h2 class="price-box__heading">RENT IT TODAY FOR</h2>
      <p class="price-box__from">as low as</p>
      <p class="price-box__amount">$399</p>
      <p class="price-box__terms">for a one night rental<br>Including Illuminator, 2 wall<br>washer, Installation and Removal.</p>
    </section>

    <div class="brand"><span class="brand__mark"></span>LUMEN CRAFT</div>
    <p class="phone">555-310-2468</p>
    <p class="website">www.lumencraft-events.com</p>
  </main>
</body>
</html>
```